University of Carrowmere Lindell Saxophone Quartet Concert

We need a poster design advertising the Lindell Saxophone Quartet Concert on Tuesday, April 23 at 5pm. The program concert will consist of 2 works by Peter Voskuilen: Harbor Lanterns and Meridian ledger. These two works should be included on the poster being the concert is featuring the composer and his works. Peter Voskuilen is known for his very "natural" sounding music. He resides in Montana and writes mostly from his small cottage in the mountains. This same idea of nature and "Montana" should be included on the poster design. He is deeply influenced by Thrane and most of the music he writes is play offs from Thrane Chorales.

The concert title is: "Where Stillness Gathers Near"

Target Market(s)

Collegiate Musician, Professional Musicians, Music Faculty

Industry/Entity Type

Advertising

Requirements
Must have
• 1. Title of the Concert: "Where Stillness Gathers Near"
2. "Lindell Saxophone Quartet Presents"
3. Date (April 23)
4. Time: 5pm
5. Location: Chapel of The Gentle Osric
Nice to have
• Nice to maybe keep the idea of "Montana" and that mountian-esque feel

```html
<!DOCTYPE html>
<html lang="en">
<head>
<meta charset="utf-8">
<title>Where Stillness Gathers Near — Lindell Saxophone Quartet</title>
<link rel="stylesheet" href="https://fonts.googleapis.com/css2?family=Saira+Stencil+One&family=Kaushan+Script&family=Oswald:wght@500;600;700&display=swap">
<style>
  :root {
    --sky-top: #1b5fcf;
    --sky-mid: #3e9ae6;
    --sky-low: #7cc0f0;
    --snow: #e4ecf4;
    --rock: #8d97a6;
    --forest: #5f9a2c;
    --meadow: #9cc23a;
    --lake: #2a8fb3;
    --reflect: #7dd13c;
    --deep: #0a1f3f;
    --shadow: #05070c;
    --white: #ffffff;
    --tag-pink: #ff2fc0;
    --venue-blue: #2b9fdc;
  }
  * { margin: 0; padding: 0; box-sizing: border-box; }
  html, body {
    width: 886px; height: 1200px; overflow: hidden;
    background: #ffffff;
  }
  .poster {
    position: relative;
    width: 886px; height: 1200px;
    overflow: hidden;
  }
  .scene-photo {
    position: absolute; inset: 0;
  }
  .concert-title {
    position: absolute;
    top: 86px; right: 72px;
    text-align: right;
    font-family: "Saira Stencil One", "Arial Black", sans-serif;
    font-size: 88px;
    line-height: 84px;
    color: var(--white);
    text-transform: uppercase;
    letter-spacing: 1px;
  }
  .presenter-line {
    position: absolute;
    top: 448px; right: 70px;
    font-family: "Kaushan Script", cursive;
    font-size: 26px;
    color: var(--white);
  }
  .program {
    position: absolute;
    right: 70px; top: 930px;
    text-align: right;
    color: var(--white);
    font-family: "Oswald", sans-serif;
    text-shadow: 0 1px 4px rgba(5, 20, 40, 0.6);
  }
  .program-composer {
    font-family: "Kaushan Script", cursive;
    font-size: 24px;
    line-height: 32px;
  }
  .program-works {
    font-weight: 500;
    font-size: 24px;
    line-height: 34px;
    text-transform: uppercase;
    letter-spacing: 1px;
  }
  .info-bar {
    position: absolute;
    left: 0; right: 0;
    top: 1078px; height: 56px;
    background: var(--white);
  }
  .date-tag {
    position: absolute;
    left: 62px; top: 1070px;
    height: 64px; width: 270px;
    background: var(--tag-pink);
    clip-path: polygon(0 0, 92% 0, 100% 50%, 92% 100%, 0 100%);
    font-family: "Oswald", sans-serif;
    font-weight: 700;
    font-size: 34px;
    color: var(--white);
    line-height: 64px;
    padding-left: 18px;
    letter-spacing: 1px;
  }
  .venue {
    position: absolute;
    right: 30px; top: 1078px;
    height: 56px; line-height: 56px;
    font-family: "Oswald", sans-serif;
    font-weight: 600;
    font-size: 32px;
    color: var(--venue-blue);
    text-transform: uppercase;
    letter-spacing: 0.5px;
  }
</style>
</head>
<body>
  <main class="poster">
    <svg class="scene-photo" width="886" height="1200" viewBox="0 0 886 1200" role="img" aria-label="Photograph of a saxophone player in silhouette on the left before snowy mountain peaks, green forested slopes and a reflecting alpine lake">
      <defs>
        <linearGradient id="landscape" x1="0" y1="0" x2="0" y2="1">
          <stop offset="0" stop-color="var(--sky-top)"/>
          <stop offset="0.3" stop-color="var(--sky-mid)"/>
          <stop offset="0.42" stop-color="var(--sky-low)"/>
          <stop offset="0.47" stop-color="var(--snow)"/>
          <stop offset="0.53" stop-color="var(--rock)"/>
          <stop offset="0.6" stop-color="var(--forest)"/>
          <stop offset="0.65" stop-color="var(--meadow)"/>
          <stop offset="0.69" stop-color="var(--lake)"/>
          <stop offset="0.76" stop-color="var(--reflect)"/>
          <stop offset="0.82" stop-color="var(--lake)"/>
          <stop offset="1" stop-color="var(--deep)"/>
        </linearGradient>
        <linearGradient id="silhouette" x1="0" y1="0" x2="1" y2="0">
          <stop offset="0" stop-color="var(--shadow)" stop-opacity="0.95"/>
          <stop offset="0.32" stop-color="var(--shadow)" stop-opacity="0.85"/>
          <stop offset="0.5" stop-color="var(--shadow)" stop-opacity="0"/>
        </linearGradient>
      </defs>
      <rect width="886" height="1200" fill="url(#landscape)"/>
      <rect width="886" height="1200" fill="url(#silhouette)"/>
    </svg>

    <h1 class="concert-title">Where<br>Stillness<br>Gathers<br>Near</h1>
    <p class="presenter-line">Lindell Saxophone Quartet Presents</p>

    <div class="program">
      <p class="program-composer">Music of Peter Voskuilen</p>
      <p class="program-works">Harbor Lanterns · Meridian Ledger</p>
    </div>

    <div class="info-bar"></div>
    <p class="date-tag">APRIL 23 5PM</p>
    <p class="venue">Chapel of The Gentle Osric</p>
  </main>
</body>
</html>
```